I need business cards for a new company called BrightHarbor Healthcare Education Consulting. We provide a comprehensive suite of consulting and education services designed to support healthcare organizations, educational institutions, pre-professionals, and professionals in achieving excellence. Our services are tailored to address the dynamic needs of the healthcare sector, from operational efficiency to workforce development and beyond. We provide customized solutions for individuals and organizations seeking to enhance knowledge, compliance, and care delivery through innovative and effective educational programs. We would like to see designs that use the colors blue and green. Tagline: "Where Learning Meets Healthcare Innovation". QR code linking to website and LinkedIn profile. If possible, reflect the consulting and education aspect of the business with symbols or phrases that emphasize guidance, learning, or expertise. Logo is attached.

```html
<!DOCTYPE html>
<html lang="en">
<head>
<meta charset="utf-8">
<title>BrightHarbor Healthcare Education Consulting – Business Cards</title>
<link rel="stylesheet" href="https://fonts.googleapis.com/css2?family=Montserrat:wght@400;500;600;700;800&display=swap">
<style>
  :root {
    --backdrop: #d9d9d9;
    --card-dark: #121212;
    --card-dark-edge: #2a2a2a;
    --card-light: #ffffff;
    --teal: #6cc3a6;
    --blue: #1f6fb2;
    --blue-tint: #e6f0f9;
    --ink: #111111;
    --ink-soft: #2b2b2b;
    --white: #ffffff;
  }
  * { box-sizing: border-box; margin: 0; padding: 0; }
  html, body {
    width: 1200px; height: 900px; overflow: hidden;
    background: var(--backdrop);
    font-family: "Montserrat", Arial, sans-serif;
  }
  .canvas {
    position: relative; width: 1200px; height: 900px;
    display: flex; flex-direction: column; align-items: center; justify-content: center; gap: 48px;
  }
  .card {
    position: relative; width: 640px; height: 366px; border-radius: 26px;
    box-shadow: 0 10px 24px rgba(0,0,0,0.18);
    overflow: hidden;
  }
  .card--front {
    background: radial-gradient(ellipse at 40% 40%, var(--card-dark-edge), var(--card-dark) 70%);
    display: flex; flex-direction: column; align-items: center; justify-content: center;
  }
  .card--front::after {
    content: ""; position: absolute; left: 0; right: 0; bottom: 0; height: 8px;
    background: linear-gradient(90deg, var(--blue), var(--teal));
  }
  .brand { display: flex; align-items: center; gap: 18px; }
  .brand__dot {
    width: 64px; height: 64px; border-radius: 50%; background: var(--teal); flex: none;
  }
  .brand__name { font-weight: 700; color: var(--white); line-height: 1.05; }
  .brand__name-main { display: block; font-size: 44px; letter-spacing: -0.5px; }
  .brand__name-sub { display: block; font-size: 13px; letter-spacing: 3.2px; text-transform: uppercase; margin-top: 6px; }
  .tagline {
    margin-top: 46px; color: var(--white); font-size: 17px; font-weight: 500; letter-spacing: 0.3px;
  }

  .card--back { background: var(--card-light); padding: 46px 44px; }
  .card--back .brand__dot { width: 70px; height: 70px; }
  .card--back .brand__name { color: var(--ink); }
  .card--back .brand__name-main { font-size: 46px; }
  .card--back .brand__name-sub { font-size: 12px; letter-spacing: 2.8px; }
  .details { display: flex; align-items: stretch; margin-top: 40px; gap: 20px; }
  .person { text-align: right; width: 200px; }
  .person__name { color: var(--teal); font-size: 25px; font-weight: 700; white-space: nowrap; }
  .person__role { color: var(--ink); font-size: 15px; font-weight: 500; margin-top: 2px; }
  .divider { width: 2px; background: var(--blue); }
  .contact { list-style: none; display: flex; flex-direction: column; gap: 6px; }
  .contact__item { display: flex; align-items: center; gap: 9px; color: var(--ink-soft); font-size: 15px; font-weight: 500; white-space: nowrap; }
  .contact__icon { width: 15px; height: 15px; flex: none; }
  .address { margin-top: 26px; margin-left: 98px; color: var(--ink); font-size: 15px; font-weight: 500; }
  .qr-area {
    position: absolute; right: 40px; bottom: 40px; width: 92px; height: 92px;
    border: 3px solid var(--blue); border-radius: 8px; background: var(--blue-tint);
  }
  .card--back::after {
    content: ""; position: absolute; left: 0; right: 0; bottom: 0; height: 8px;
    background: linear-gradient(90deg, var(--teal), var(--blue));
  }
</style>
</head>
<body>
<main class="canvas">
  <section class="card card--front" aria-label="Card front">
    <div class="brand">
      <span class="brand__dot"></span>
      <p class="brand__name">
        <span class="brand__name-main">BrightHarbor</span>
        <span class="brand__name-sub">Healthcare Education Consulting</span>
      </p>
    </div>
    <p class="tagline">Where Learning Meets Healthcare Innovation</p>
  </section>

  <section class="card card--back" aria-label="Card back">
    <div class="brand">
      <span class="brand__dot"></span>
      <p class="brand__name">
        <span class="brand__name-main">BrightHarbor</span>
        <span class="brand__name-sub">Healthcare Education Consulting</span>
      </p>
    </div>
    <div class="details">
      <div class="person">
        <p class="person__name">Dana Whitfield</p>
        <p class="person__role">Managing Director</p>
      </div>
      <span class="divider"></span>
      <ul class="contact">
        <li class="contact__item">
          <svg class="contact__icon" viewBox="0 0 16 16"><path d="M3 1.5l2.5 0 1.2 3.2-1.6 1.2a8 8 0 0 0 5 5l1.2-1.6 3.2 1.2v2.5c0 .8-.7 1.5-1.5 1.5C6.8 14.5 1.5 9.2 1.5 3c0-.8.7-1.5 1.5-1.5z" fill="var(--blue)"/></svg>
          555-014-2288
        </li>
        <li class="contact__item">
          <svg class="contact__icon" viewBox="0 0 16 16"><rect x="1" y="3" width="14" height="10" rx="1" fill="var(--blue)"/><path d="M1.5 3.5L8 9l6.5-5.5" stroke="#fff" stroke-width="1.3" fill="none"/></svg>
          info@brightharbor.example
        </li>
        <li class="contact__item">
          <svg class="contact__icon" viewBox="0 0 16 16"><circle cx="8" cy="8" r="6.5" fill="none" stroke="var(--blue)" stroke-width="1.5"/><path d="M1.5 8h13M8 1.5c-3 3.5-3 9.5 0 13M8 1.5c3 3.5 3 9.5 0 13" stroke="var(--blue)" stroke-width="1.2" fill="none"/></svg>
          www.brightharbor.example
        </li>
      </ul>
    </div>
    <p class="address">48 Cedar Lane Springfield, ST 00000</p>
    <div class="qr-area" role="img" aria-label="QR code linking to website and LinkedIn profile"></div>
  </section>
</main>
</body>
</html>
```